Business cards, e-mail signature, letterhead
Noral Studio, Inc
Business cards, e-mail signature, letterhead - Communications and Media
Creative Brief
Bright & Fun-filled
Tobin Varley
President, Noral Studio Inc.
Card: New York City Letterhead: 47 West 112th St. 9F New York, NY 10031
skype: tobinvarley604
tbnvrl@quillpost.net
www.NoralStudio.com
Locations of our properties can be listed on the back of card (see below) and incorporated into letterhead.
Ash Fork, AZ / Ashtabula, OH/ Belle Rose, LA/ Blanca, CO/ Cross City, FL/ Dulac, LA/ Huntington, OR/ Islamorada, FL/ Lead, SD/ Mona, UT/ Morgan, GA/ Ty Ty, GA/ Winchester, VA

```html
<!DOCTYPE html>
<html lang="en">
<head>
<meta charset="utf-8">
<title>Noral Studio, Inc — Business Card</title>
<link rel="stylesheet" href="https://fonts.googleapis.com/css2?family=Open+Sans:wght@400;600;700&display=swap">
<style>
  :root {
    --navy: #1f2a7a;
    --grey: #8a8d93;
    --grey-light: #c9cbcf;
    --ink: #333740;
    --paper: #ffffff;
    --stage: #e7e8eb;
  }
  * { box-sizing: border-box; margin: 0; padding: 0; }
  html, body { width: 1200px; height: 864px; overflow: hidden; }
  body {
    background: var(--stage);
    font-family: "Open Sans", Arial, sans-serif;
    display: flex;
    align-items: center;
    justify-content: center;
    gap: 50px;
  }
  .card {
    position: relative;
    width: 540px;
    height: 310px;
    background: var(--paper);
    border-radius: 18px;
    overflow: hidden;
    box-shadow: 0 6px 20px rgba(0,0,0,.12);
  }

  /* Front */
  .card-front .brand {
    position: absolute;
    left: 0; right: 0; top: 92px;
    display: flex;
    flex-direction: column;
    align-items: center;
    gap: 14px;
  }
  .brand-dot {
    width: 70px; height: 70px;
    border-radius: 50%;
    background: var(--navy);
    flex: none;
  }
  .brand-name {
    font-weight: 700;
    font-size: 22px;
    color: var(--navy);
    letter-spacing: .5px;
    white-space: nowrap;
  }
  .card-front .domain {
    position: absolute;
    left: 0; right: 0; bottom: 44px;
    text-align: center;
    font-size: 12px;
    letter-spacing: 3px;
    color: var(--grey);
  }

  /* Back */
  .swoosh { position: absolute; left: 0; bottom: 0; width: 540px; height: 120px; }
  .contact {
    position: absolute;
    left: 276px; top: 36px;
    color: var(--ink);
    font-size: 11px;
    line-height: 1.6;
    white-space: nowrap;
  }
  .contact .person { font-weight: 700; font-size: 14px; color: var(--navy); }
  .contact .role { margin-bottom: 8px; }
  .contact-row { display: flex; align-items: center; gap: 8px; }
  .contact-row svg { width: 13px; height: 13px; flex: none; }
  .card-back .brand {
    position: absolute;
    left: 26px; bottom: 52px;
    display: flex;
    align-items: center;
    gap: 12px;
  }
  .card-back .brand-dot { width: 48px; height: 48px; }
  .card-back .brand-text { display: flex; flex-direction: column; }
  .card-back .brand-name { font-size: 19px; }
  .tagline { font-size: 10px; color: var(--grey); letter-spacing: 1px; }
</style>
</head>
<body>

<section class="card card-front">
  <div class="brand">
    <span class="brand-dot"></span>
    <span class="brand-name">Noral Studio</span>
  </div>
  <p class="domain">www.NoralStudio.com</p>
</section>

<section class="card card-back">
  <svg class="swoosh" viewBox="0 0 540 120" preserveAspectRatio="none">
    <path d="M0 120 V100 C220 112 400 70 540 8 V120 Z" fill="var(--grey-light)"/>
    <path d="M0 120 V108 C220 118 400 82 540 30 V120 Z" fill="var(--grey)"/>
    <path d="M0 120 V114 C220 122 400 94 540 48 V120 Z" fill="var(--navy)"/>
  </svg>

  <div class="contact">
    <p class="person">Tobin Varley</p>
    <p class="role">President, Noral Studio Inc.</p>
    <p class="contact-row">
      <svg viewBox="0 0 12 12"><path d="M6 0.5a4 4 0 0 0-4 4c0 3 4 7 4 7s4-4 4-7a4 4 0 0 0-4-4z" fill="var(--navy)"/><circle cx="6" cy="4.5" r="1.5" fill="#fff"/></svg>
      47 West 112th St. 9F New York, NY 10031
    </p>
    <p class="contact-row">
      <svg viewBox="0 0 12 12"><circle cx="6" cy="6" r="6" fill="var(--navy)"/><path d="M4 3.2l1.1 1.6-.6.8c.5 1 1.1 1.6 2 2l.8-.6 1.6 1.1-.6 1.1C6 9 3.1 6.1 2.9 3.8z" fill="#fff"/></svg>
      (917) 555-0182
    </p>
    <p class="contact-row">
      <svg viewBox="0 0 12 12"><circle cx="6" cy="6" r="6" fill="var(--navy)"/></svg>
      tobinvarley604
    </p>
    <p class="contact-row">
      <svg viewBox="0 0 12 12"><circle cx="6" cy="6" r="6" fill="var(--navy)"/><path d="M3 4h6v4.2H3z" fill="#fff"/><path d="M3 4l3 2.3L9 4" stroke="var(--navy)" stroke-width=".8" fill="none"/></svg>
      tbnvrl@quillpost.net
    </p>
    <p class="contact-row">
      <svg viewBox="0 0 12 12"><circle cx="6" cy="6" r="6" fill="var(--navy)"/><circle cx="6" cy="6" r="3.3" stroke="#fff" stroke-width=".8" fill="none"/><path d="M2.7 6h6.6M6 2.7v6.6" stroke="#fff" stroke-width=".8"/></svg>
      www.NoralStudio.com
    </p>
  </div>

  <div class="brand">
    <span class="brand-dot"></span>
    <div class="brand-text">
      <span class="brand-name">NORAL STUDIO INC.</span>
      <span class="tagline">Media...refined</span>
    </div>
  </div>
</section>

</body>
</html>
```